Founder / concept developer needs business card // Consultant needs VCARD

I need a business card for me as a founding consultant in Berlin. I advise entrepreneurs, especially in the design of business ideas, business plans or financing applications. More information about this in the annexes. My USP: I design / structure complex ideas and projects convincingly so that my client is successful. I want to communicate professionalism, effectiveness and clarity. Colors like from the range BLACK-GRAY-GREEN. I am 27 years old, I have studied business for 7 years. Attachments: - Business card design (only idea, do not focus on it) - Website screenshot (only idea, do not focus on it)

Target Market(s)

Target group: Founder (20-50 yrs, m / w, needy, in "break-up phase") and CONTRACTOR / "financier" (30-55 yrs, m / w, often public service "routine-oriented"). The foundations are in quite different industries: digital, craft, tourism, retail, services, etc. Almost all German.

Industry/Entity Type

Consultant

Contact Information for Business Card

Lukas Brenner
M. Sc., International Business Administration
Gründungsberater, Konzeptentwickler
www.falkor-plan.de
kontakt@falkor-plan.de
Tel. 0157 284 3361

Colors

Designer to choose colors to be used in the design.

Requirements
Must have
• Professionalism, persuasiveness, clarity
Nice to have
• memorability
Should not have
• Schnörkelei

```html
<!DOCTYPE html>
<html lang="de">
<head>
<meta charset="utf-8">
<title>Lukas Brenner – Visitenkarte</title>
<link href="https://fonts.googleapis.com/css2?family=Roboto:wght@300;400;500&display=swap" rel="stylesheet">
<style>
  :root {
    --page-bg: #eceeef;
    --card-dark: #131718;
    --card-mid: #22282a;
    --band-gray: #2e3132;
    --brand-green: #3b8f3e;
    --name-green: #3fae45;
    --text-light: #e9ecec;
    --text-muted: #a7adae;
    --rule: #5a6062;
  }
  * { box-sizing: border-box; margin: 0; padding: 0; }
  html, body {
    width: 1200px; height: 800px; overflow: hidden;
    background: var(--page-bg);
    font-family: "Roboto", Arial, sans-serif;
  }
  .business-card {
    position: absolute; left: 150px; top: 120px;
    width: 900px; height: 560px;
    background: radial-gradient(ellipse at 45% 40%, var(--card-mid) 0%, var(--card-dark) 75%);
    box-shadow: 0 18px 40px rgba(0,0,0,0.22);
    overflow: hidden;
  }
  .side-band {
    position: absolute; top: 0; right: 72px;
    width: 70px; height: 100%;
    background: var(--band-gray);
  }
  .accent-band {
    position: absolute; top: 0; right: 0;
    width: 72px; height: 100%;
    background: var(--brand-green);
  }
  .card-content {
    position: absolute; left: 200px; top: 205px; width: 460px;
  }
  .person-name {
    font-weight: 500; font-size: 40px; letter-spacing: 0.5px;
    color: var(--name-green); text-transform: uppercase;
    margin-left: 14px;
  }
  .degree {
    font-weight: 300; font-size: 17px; color: var(--text-muted);
    margin-top: 6px;
  }
  .divider {
    width: 410px; height: 1px; background: var(--rule);
    margin: 14px 0 0 -14px;
  }
  .role {
    font-weight: 400; font-size: 17px; color: var(--text-light);
    margin: 22px 0 0 38px;
  }
  .contact-list { list-style: none; margin: 20px 0 0 38px; }
  .contact-list li {
    display: flex; align-items: center; gap: 18px;
    font-size: 22px; letter-spacing: 0.8px; color: var(--text-light);
    line-height: 27px;
  }
  .contact-list svg { width: 20px; height: 20px; flex: none; }
</style>
</head>
<body>
  <div class="business-card">
    <div class="side-band"></div>
    <div class="accent-band"></div>
    <div class="card-content">
      <h1 class="person-name">Lukas Brenner</h1>
      <p class="degree">(M. Sc.) International Business Administration</p>
      <div class="divider"></div>
      <p class="role">Gründungsberater, Konzeptentwickler</p>
      <ul class="contact-list">
        <li>
          <svg viewBox="0 0 24 24" aria-hidden="true"><path fill="#3fae45" d="M6.6 10.8a15.1 15.1 0 0 0 6.6 6.6l2.2-2.2c.3-.3.7-.4 1-.2 1.1.4 2.3.6 3.6.6.6 0 1 .4 1 1V20c0 .6-.4 1-1 1A17 17 0 0 1 3 4c0-.6.4-1 1-1h3.5c.6 0 1 .4 1 1 0 1.3.2 2.5.6 3.6.1.3 0 .7-.2 1z"/></svg>
          <span>0157 284 3361</span>
        </li>
        <li>
          <svg viewBox="0 0 24 24" aria-hidden="true"><rect x="3" y="5.5" width="18" height="13" fill="none" stroke="#3fae45" stroke-width="2"/><path d="M3 6l9 7 9-7" fill="none" stroke="#3fae45" stroke-width="2"/></svg>
          <span>kontakt@falkor-plan.de</span>
        </li>
        <li>
          <svg viewBox="0 0 24 24" aria-hidden="true"><g fill="none" stroke="#3fae45" stroke-width="1.8"><circle cx="12" cy="12" r="9"/><ellipse cx="12" cy="12" rx="4" ry="9"/><path d="M3 12h18M4.5 7.5h15M4.5 16.5h15"/></g></svg>
          <span>www.falkor-plan.de</span>
        </li>
      </ul>
    </div>
  </div>
</body>
</html>
```